I am a Life Coaching and I have purchased the logo for my business. I need business cards

I need a business card design using the logo attached (but instead of the logo saying "Harbor" I need it to say "Bright Meadow Coaching"

Target Market(s)

Middle-aged people

Industry/Entity Type

Life coaching

Contact Information for Business Card

Name, email address, phone number, website

Font styles to use
Serif
Sans Serif
Script

Colors
0094D4
00A9DD
6FCCEA
C7EBF8
E9F6FB
00AB8E
00BBA5
67D7C9
C6EFE9
E9F9F6
59FF00
82FF00
B8FF75
E3FFCB
F4FFEA

Requirements
Must have
• Logo and contact info above
Nice to have
• As close to the business card inspo attached as possible

```html
<!DOCTYPE html>
<html lang="en">
<head>
<meta charset="utf-8">
<title>Bright Meadow Coaching – Business Card</title>
<link rel="stylesheet" href="https://fonts.googleapis.com/css2?family=Roboto:wght@400;500&display=swap">
<style>
  :root {
    --page-bg: #ecebe8;
    --card-bg: #ffffff;
    --ink: #3d3d3d;
    --ink-soft: #555555;
    --accent: #9fd6e6;
    --accent-strong: #6fcce9;
    --deco-grey: #d6d6d6;
    --card-shadow: 0 10px 28px rgba(0, 0, 0, 0.18);
  }
  * { box-sizing: border-box; margin: 0; padding: 0; }
  html, body {
    width: 1200px;
    height: 1200px;
    overflow: hidden;
    background: var(--page-bg);
    font-family: "Roboto", sans-serif;
    color: var(--ink);
  }
  .canvas {
    position: relative;
    width: 1200px;
    height: 1200px;
  }
  .card {
    position: absolute;
    left: 219px;
    width: 762px;
    height: 433px;
    background: var(--card-bg);
    box-shadow: var(--card-shadow);
    overflow: hidden;
  }
  .card--front { top: 127px; }
  .card--back { top: 637px; }

  /* Front */
  .brand {
    position: absolute;
    left: 0;
    right: 0;
    top: 188px;
    display: flex;
    align-items: center;
    justify-content: center;
    gap: 14px;
  }
  .brand__dot {
    width: 22px;
    height: 22px;
    border-radius: 50%;
    background: var(--accent);
  }
  .brand__name {
    font-size: 34px;
    font-weight: 500;
    color: var(--ink);
    letter-spacing: 0.5px;
  }
  .website {
    position: absolute;
    left: 0;
    right: 0;
    top: 390px;
    text-align: center;
    font-size: 18px;
    letter-spacing: 1.4px;
    color: var(--ink-soft);
  }

  /* Back */
  .back-decoration {
    position: absolute;
    left: -40px;
    top: 65px;
    width: 410px;
    height: 410px;
    border-radius: 50%;
    background: radial-gradient(circle, rgba(214,214,214,0.15) 0%, rgba(214,214,214,0.75) 45%, rgba(214,214,214,0.25) 70%, rgba(255,255,255,0) 100%);
  }
  .person {
    position: absolute;
    right: 68px;
    top: 208px;
    text-align: right;
  }
  .person__name {
    font-size: 23px;
    line-height: 28px;
    color: var(--ink);
  }
  .person__role {
    font-size: 19px;
    line-height: 24px;
    color: var(--ink-soft);
  }
  .person-bar {
    position: absolute;
    left: 711px;
    top: 212px;
    width: 4px;
    height: 45px;
    background: var(--accent);
  }
  .contact-list {
    position: absolute;
    right: 38px;
    top: 278px;
    list-style: none;
  }
  .contact-list__item {
    display: flex;
    align-items: center;
    justify-content: flex-end;
    gap: 10px;
    height: 27.8px;
    font-size: 19px;
    color: var(--ink);
  }
  .contact-list__icon {
    width: 20px;
    height: 20px;
    flex: none;
  }
</style>
</head>
<body>
<main class="canvas">

  <section class="card card--front" aria-label="Card front">
    <div class="brand">
      <span class="brand__dot" aria-hidden="true"></span>
      <span class="brand__name">Bright Meadow Coaching</span>
    </div>
    <p class="website">www.brightmeadow.com</p>
  </section>

  <section class="card card--back" aria-label="Card back">
    <div class="back-decoration" role="img" aria-label="Large faint brand symbol decoration"></div>

    <div class="person">
      <p class="person__name">Clara Hensley</p>
      <p class="person__role">Coach</p>
    </div>
    <span class="person-bar" aria-hidden="true"></span>

    <ul class="contact-list">
      <li class="contact-list__item">
        <span>555 - 01234 05678</span>
        <svg class="contact-list__icon" viewBox="0 0 20 20" aria-hidden="true">
          <circle cx="10" cy="10" r="8.6" fill="none" stroke="var(--accent)" stroke-width="1.4"/>
          <path d="M7 5.8c.5-.4 1-.3 1.3.2l.8 1.4c.2.4.1.8-.2 1.1l-.6.5c.5 1.1 1.3 1.9 2.4 2.4l.5-.6c.3-.3.7-.4 1.1-.2l1.4.8c.5.3.6.8.2 1.3l-.6.7c-.6.6-1.6.6-2.6.1-1.8-.9-3.2-2.3-4.1-4.1-.5-1-.5-2 .1-2.6z" fill="var(--accent)"/>
        </svg>
      </li>
      <li class="contact-list__item">
        <span>c.hensley@mailbox</span>
        <svg class="contact-list__icon" viewBox="0 0 20 20" aria-hidden="true">
          <rect x="1.5" y="4" width="17" height="12" rx="1.5" fill="none" stroke="var(--accent)" stroke-width="1.4"/>
          <path d="M2 5l8 6 8-6" fill="none" stroke="var(--accent)" stroke-width="1.4"/>
        </svg>
      </li>
      <li class="contact-list__item">
        <span>clara.hensley</span>
        <svg class="contact-list__icon" viewBox="0 0 20 20" aria-hidden="true">
          <circle cx="10" cy="10" r="8.6" fill="none" stroke="var(--accent)" stroke-width="1.4"/>
        </svg>
      </li>
      <li class="contact-list__item">
        <span>clara.hensley</span>
        <svg class="contact-list__icon" viewBox="0 0 20 20" aria-hidden="true">
          <circle cx="10" cy="10" r="8.6" fill="none" stroke="var(--accent)" stroke-width="1.4"/>
        </svg>
      </li>
      <li class="contact-list__item">
        <span>88, Pine Avenue, Portland</span>
        <svg class="contact-list__icon" viewBox="0 0 20 20" aria-hidden="true">
          <path d="M10 1.5c-3.3 0-6 2.6-6 5.9 0 4.3 6 11.1 6 11.1s6-6.8 6-11.1c0-3.3-2.7-5.9-6-5.9z" fill="var(--accent)"/>
          <circle cx="10" cy="7.4" r="2.2" fill="#ffffff"/>
        </svg>
      </li>
    </ul>
  </section>

</main>
</body>
</html>
```